Die Designerin hat meine Vorstellungen am besten verstanden und umgesetzt. Sie war mir gegenüber sehr verständnisvoll und entgegenkommend. Die Kommunikation mit ihr war sehr erfreulich und sympathisch. Bei meinem nächsten Projekt werde ich mich zuerst an sie wenden.

```html
<!DOCTYPE html>
<html lang="de">
<head>
<meta charset="utf-8">
<title>Mein wundersamer Sommer in Kranzbühl – Buchumschlag</title>
<link rel="stylesheet" href="https://fonts.googleapis.com/css2?family=Noto+Serif:wght@400;700&display=swap">
<style>
  :root {
    --backdrop: #922a2a;
    --cover-paper: #e4e4e6;
    --spine-paper: #d6d7da;
    --accent-red: #d8232e;
    --title-white: #fbfbfb;
    --sky-blue: #c9dde8;
    --scooter-red: #e0594a;
    --muted-grey: #9b9ea3;
  }
  * { margin: 0; padding: 0; box-sizing: border-box; }
  html, body {
    width: 1200px;
    height: 1055px;
    overflow: hidden;
    background: var(--backdrop);
  }
  .canvas {
    position: relative;
    width: 1200px;
    height: 1055px;
    background: var(--backdrop);
  }
  .cover {
    position: absolute;
    left: 366px;
    top: 281px;
    width: 330px;
    height: 490px;
    background: var(--cover-paper);
    overflow: hidden;
    font-family: "Noto Serif", Georgia, serif;
  }
  .cover__sky {
    position: absolute;
    left: 150px;
    top: -20px;
    width: 230px;
    height: 110px;
    border-radius: 0 0 0 120px;
    background: var(--sky-blue);
    opacity: 0.55;
  }
  .cover__illustration {
    position: absolute;
    left: 28px;
    top: 143px;
    width: 262px;
    height: 272px;
    border-radius: 30px;
    background: linear-gradient(180deg, #dfe6eb 0%, #e6c3bd 45%, #e58a7e 75%, #dfe2e6 100%);
  }
  .cover__genre {
    position: absolute;
    top: 8px;
    width: 100%;
    text-align: center;
    font-size: 14px;
    color: var(--accent-red);
    font-weight: 400;
  }
  .cover__title {
    position: absolute;
    top: 28px;
    left: 0;
    width: 100%;
    text-align: center;
    font-weight: 700;
    font-size: 27px;
    letter-spacing: 0.3em;
    line-height: 73.5px;
    color: var(--title-white);
    text-shadow: 1px 1px 0 var(--accent-red), 2px 2px 0 var(--accent-red);
  }
  .cover__title span { display: block; padding-left: 0.3em; }
  .cover__author {
    position: absolute;
    top: 446px;
    width: 100%;
    text-align: center;
    font-size: 12.5px;
    font-weight: 700;
    letter-spacing: 0.32em;
    padding-left: 0.32em;
    color: var(--accent-red);
  }
  .spine {
    position: absolute;
    left: 763px;
    top: 279px;
    width: 58px;
    height: 493px;
    background: var(--spine-paper);
    font-family: "Noto Serif", Georgia, serif;
  }
  .spine__title {
    position: absolute;
    left: 50%;
    top: 32px;
    writing-mode: vertical-rl;
    transform: translateX(-50%);
    font-size: 17px;
    font-weight: 700;
    letter-spacing: 0.06em;
    color: var(--accent-red);
    white-space: nowrap;
  }
  .spine__author {
    position: absolute;
    bottom: 12px;
    width: 100%;
    text-align: center;
    font-size: 8px;
    line-height: 11px;
    color: var(--muted-grey);
  }
</style>
</head>
<body>
<main class="canvas">
  <section class="cover">
    <div class="cover__sky"></div>
    <div class="cover__illustration" role="img" aria-label="Illustration: Fahrer auf einem roten Motorroller mit Lieferbox vor hellblauem Himmel"></div>
    <p class="cover__genre">ROMAN</p>
    <h1 class="cover__title">
      <span>Mein</span>
      <span>wundersamer</span>
      <span>Sommer</span>
      <span>in</span>
      <span>Kranzbühl</span>
    </h1>
    <p class="cover__author">BERNHARD KOLWITZ</p>
  </section>
  <aside class="spine">
    <p class="spine__title">Mein wundersamer Sommer in Kranzbühl</p>
    <p class="spine__author">BERNHARD<br>KOLWITZ</p>
  </aside>
</main>
</body>
</html>
```